International Freight Forwarder need a business card

We need a logo design for a freight forwarding company . We are active in Sea Transportation, Truck transportation, and Air Transportation, The design should be have normal dimensions of a card and should not have cuts and holes in its design (printed design is required - lamination accepted)

The said company is agent and sales representative of 2 other Shipping companies (whose logos, name, and website should also be mentioned on the card)

Industry/Entity Type

Logistics

Contact Information for Business Card

Address is "No.7, 2nd Sarv Baghestan-e-Nouri, Tehran, IR
Tel number is +98 21 66394512
Fax number is +98 21 66395830
E-Mail address is info@roshanbarsaz.com
Website is www.roshanbarsaz.com

Open Layer Logos attached as well

Colors
33a6d7
0292cd
0255a3
3276b5
85abd2
85cae6
cee9f5
d5e2ee
ffffff

Requirements
Must have
• Main logo of Roshan Barsaz
• Logo of TQM Shipping Line
• London, United Kingdom
• tqmline.com
• Logo of Calm Reef Shipping
• Dubai, United Arab Emirates
• crsuae.com
• We require OPEN layer file to be submitted to us upon project selection.
Should not have
• Weird Designs such as cuts to the shape or holes in design.

```html
<!DOCTYPE html>
<html lang="en">
<head>
<meta charset="utf-8">
<title>Roshan Barsaz – Business Card</title>
<link href="https://fonts.googleapis.com/css2?family=Open+Sans:wght@400;600;700&display=swap" rel="stylesheet">
<style>
  :root {
    --sky: #5fcbea;
    --azure: #33a6d7;
    --ocean: #3276b5;
    --navy: #0255a3;
    --deep: #1f3f86;
    --ink: #4a4f57;
    --paper: #ffffff;
    --ground: #e9eef3;
  }
  * { box-sizing: border-box; margin: 0; padding: 0; }
  html, body {
    width: 1200px; height: 900px; overflow: hidden;
    background: var(--ground);
    font-family: "Open Sans", Arial, sans-serif;
  }
  .stage {
    position: relative; width: 1200px; height: 900px;
    display: flex; flex-direction: column; align-items: center; justify-content: center; gap: 40px;
  }
  .card {
    position: relative; width: 680px; height: 388px; overflow: hidden;
    box-shadow: 0 8px 24px rgba(0,0,0,.15);
  }

  /* Back: partner lines */
  .card-back {
    background: linear-gradient(100deg, var(--sky) 0%, var(--azure) 45%, var(--ocean) 100%);
    color: var(--paper);
  }
  .card-back .divider {
    position: absolute; left: 340px; top: 70px; width: 1px; height: 250px;
    background: rgba(255,255,255,.55); transform: rotate(-18deg);
  }
  .partner {
    position: absolute; width: 260px; text-align: center;
  }
  .partner-left { left: 60px; top: 120px; }
  .partner-right { left: 370px; top: 80px; }
  .partner-mark {
    display: flex; align-items: center; justify-content: center; gap: 10px;
    font-weight: 700; font-size: 17px; margin-bottom: 14px;
  }
  .partner-mark .dot {
    width: 34px; height: 34px; border-radius: 50%; background: var(--paper);
  }
  .partner-city { font-size: 17px; line-height: 1.3; }
  .partner-web { font-size: 17px; font-weight: 700; letter-spacing: 1px; margin-top: 10px; }

  /* Front: company */
  .card-front { background: var(--paper); }
  .card-front .shapes { position: absolute; inset: 0; }
  .brand {
    position: absolute; right: 60px; top: 60px; width: 200px;
    display: flex; flex-direction: column; align-items: center; gap: 12px;
  }
  .brand .ring {
    width: 110px; height: 110px; border-radius: 50%;
    border: 2px solid #9aa3ad;
  }
  .brand-name {
    font-weight: 700; font-size: 15px; color: var(--navy); text-align: center; line-height: 1.25;
  }
  .contact {
    position: absolute; left: 70px; bottom: 36px; color: var(--ink);
  }
  .person { font-weight: 700; font-size: 20px; color: var(--deep); }
  .role { font-size: 20px; color: var(--azure); margin-bottom: 6px; }
  .address { font-size: 15px; line-height: 1.35; margin-bottom: 4px; }
  .line { display: flex; align-items: center; gap: 10px; font-size: 15px; line-height: 1.5; }
  .line svg { width: 14px; height: 14px; fill: var(--deep); flex: none; }
</style>
</head>
<body>
<main class="stage">

  <section class="card card-back" aria-label="Card back with partner shipping lines">
    <div class="divider"></div>
    <div class="partner partner-left">
      <div class="partner-mark"><span class="dot"></span>TQM Shipping Line</div>
      <p class="partner-city">TQM Shipping Line London<br>United Kingdom</p>
      <p class="partner-web">www.tqmline.com</p>
    </div>
    <div class="partner partner-right">
      <div class="partner-mark"><span class="dot"></span>Calm Reef Shipping</div>
      <p class="partner-city">Calm Reef ShippingDubai<br>United Arab Emirates</p>
      <p class="partner-web">www.crsuae.com</p>
    </div>
  </section>

  <section class="card card-front" aria-label="Card front with contact details">
    <svg class="shapes" viewBox="0 0 680 388" preserveAspectRatio="none">
      <polygon points="0,0 150,0 0,115" fill="var(--deep)"/>
      <polygon points="680,140 680,388 540,388" fill="var(--ocean)"/>
    </svg>

    <div class="brand">
      <span class="ring"></span>
      <p class="brand-name">Roshan Barsaz<br>International<br>Transport.Co L.L.c</p>
    </div>

    <div class="contact">
      <p class="person">DANIEL REYES</p>
      <p class="role">CEO/FOUNDER</p>
      <p class="address">No.7, 2nd Sarv<br>Baghestan-e-Nouri, Tehran, IR</p>
      <p class="line"><svg viewBox="0 0 16 16"><path d="M3 1h3l1.5 4-2 1.3a9 9 0 0 0 4.2 4.2L11 8.5l4 1.5v3a2 2 0 0 1-2 2A12 12 0 0 1 1 3a2 2 0 0 1 2-2z"/></svg>+98 21 66394512</p>
      <p class="line"><svg viewBox="0 0 16 16"><path d="M4 1h8v4H4zM1 6h14v7h-3v2H4v-2H1zm4 4v4h6v-4z"/></svg>+98 21 66395830</p>
      <p class="line"><svg viewBox="0 0 16 16"><path d="M1 3h14v10H1zm1.5 1.5L8 9l5.5-4.5z"/></svg>info@roshanbarsaz.com</p>
      <p class="line"><svg viewBox="0 0 16 16"><circle cx="8" cy="8" r="7"/></svg>www.roshanbarsaz.com</p>
    </div>
  </section>

</main>
</body>
</html>
```